Bright Album Android app screenshots

I need some screenshot backgrounds that will be used as a background for Bright Album at https://apps.quorvane.com/store/apps/details?id=com.brightpocketkit.album&hl=en-GB . I want to replace that boring orange background with something more exciting, maybe put some icons related to galleries there. Something like https://apps.quorvane.com/store/apps/details?id=com.brightpocketkit.calendar&hl=en-US has been done for the calendar. Let's keep it orange #F57C00 though and the resolution should be 2000x3555, I need 4 slightly different variants. Only the top and the sides of the background will be visible so focus on those parts. I need only the orange backgrounds, not the actual device or screenshot itself.

```html
<!DOCTYPE html>
<html lang="en">
<head>
<meta charset="utf-8">
<title>Bright Album – store screenshots</title>
<link rel="stylesheet" href="https://fonts.googleapis.com/css2?family=Poppins:wght@700&family=Roboto:wght@400;500&display=swap">
<style>
  :root {
    --page: #ffffff;
    --orange: #f57c00;
    --orange-deep: #e96f00;
    --orange-bar: #f27a00;
    --wave: rgba(200, 70, 40, 0.22);
    --icon: rgba(255, 214, 180, 0.55);
    --white: #ffffff;
    --device: #111111;
  }
  * { box-sizing: border-box; margin: 0; padding: 0; }
  html, body { width: 1200px; height: 667px; overflow: hidden; background: var(--page); }
  .canvas { position: relative; width: 1200px; height: 667px; }

  .panel {
    position: absolute; top: 123px; width: 245px; height: 435px;
    background: var(--orange); overflow: hidden;
    box-shadow: 0 2px 5px rgba(0,0,0,0.18);
  }
  .panel--ads { left: 74px; }
  .panel--editor { left: 342px; }
  .panel--custom { left: 611px; }
  .panel--secure { left: 880px; }

  .wave-band {
    position: absolute; left: -20px; top: 10px; width: 290px; height: 130px;
    background: radial-gradient(ellipse at 60% 40%, var(--wave), transparent 70%);
  }
  .feature-icon { position: absolute; top: 8px; right: 10px; width: 86px; height: 86px; }
  .title {
    position: absolute; left: 0; right: 0; top: 36px; text-align: center;
    font-family: "Poppins", sans-serif; font-weight: 700; font-size: 25px;
    color: var(--white); letter-spacing: 0.2px;
    text-shadow: 0 1px 2px rgba(0,0,0,0.25);
  }

  .device {
    position: absolute; left: 29px; top: 95px; width: 187px; height: 345px;
    background: var(--device); border-radius: 16px 16px 0 0; padding: 6px 6px 0;
  }
  .screen { width: 100%; height: 100%; border-radius: 10px 10px 0 0; overflow: hidden; background: #222; }
  .status-bar {
    height: 12px; background: var(--orange-deep); display: flex; justify-content: flex-end;
    align-items: center; gap: 4px; padding-right: 8px;
    font-family: "Roboto", sans-serif; font-size: 6.5px; color: var(--white);
  }
  .status-bar svg { width: 6px; height: 6px; }
  .app-bar {
    height: 24px; background: var(--orange-bar); display: flex; align-items: center;
    padding: 0 8px 0 9px; font-family: "Roboto", sans-serif; font-size: 9px; color: var(--white);
  }
  .app-bar .name { flex: 1; }
  .app-bar svg { width: 8px; height: 8px; margin-left: 10px; }
  .grid { display: grid; grid-template-columns: 1fr 1fr; grid-auto-rows: 88px; }
  .tile { position: relative; }
  .tile .label {
    position: absolute; left: 3px; bottom: 3px; font-family: "Roboto", sans-serif;
    font-size: 5.5px; line-height: 1.2; color: var(--white);
  }
  .t-scenery { background: linear-gradient(#b8401e, #5a3a36 60%, #3a3a44); }
  .t-garden { background: linear-gradient(#3f8a2a, #c8406a 50%, #e05a20); }
  .t-animal { background: linear-gradient(#b8c4cc, #a8683a 55%, #8a8078); }
  .t-hiking { background: linear-gradient(#cfcdb8, #7a7c5a 60%, #4a4a38); }
  .t-cute { background: linear-gradient(135deg, #c01818, #8aa020 55%, #3a5a2a); }
  .t-kids { background: linear-gradient(#c8c4bc, #a8a098); }
  .t-ruins { background: linear-gradient(#a8a49a, #7a766c); }
  .t-city { background: linear-gradient(#7aaee0, #b8703a); }
</style>
</head>
<body>
<main class="canvas">

  <section class="panel panel--ads">
    <div class="wave-band"></div>
    <svg class="feature-icon" viewBox="0 0 86 86" aria-hidden="true">
      <circle cx="43" cy="43" r="36" fill="none" stroke="var(--icon)" stroke-width="7"/>
      <line x1="18" y1="68" x2="68" y2="18" stroke="var(--icon)" stroke-width="7"/>
    </svg>
    <h2 class="title">NO Ads</h2>
    <div class="device"><div class="screen">
      <div class="status-bar"><svg viewBox="0 0 6 6"><path d="M0 0h6L3 5z" fill="#fff"/></svg><svg viewBox="0 0 6 6"><path d="M6 0v6H0z" fill="#fff"/></svg><svg viewBox="0 0 6 6"><rect x="1.5" y="0" width="3" height="6" fill="#fff"/></svg><span>12:30</span></div>
      <div class="app-bar"><span class="name">Gallery</span><svg viewBox="0 0 8 8"><circle cx="3.2" cy="3.2" r="2.3" fill="none" stroke="#fff"/><line x1="5" y1="5" x2="7.5" y2="7.5" stroke="#fff"/></svg><svg viewBox="0 0 8 8"><circle cx="4" cy="1" r=".8" fill="#fff"/><circle cx="4" cy="4" r=".8" fill="#fff"/><circle cx="4" cy="7" r=".8" fill="#fff"/></svg></div>
      <div class="grid">
        <div class="tile t-scenery" role="img" aria-label="Sunset over a rocky coast"><span class="label">Scenery<br>276</span></div>
        <div class="tile t-garden" role="img" aria-label="Field of tulips"><span class="label">Garden<br>38</span></div>
        <div class="tile t-animal" role="img" aria-label="Puppy sitting on rocks"><span class="label">Animal<br>69</span></div>
        <div class="tile t-hiking" role="img" aria-label="Hiker in misty mountains"><span class="label">Hiking<br>154</span></div>
        <div class="tile t-cute" role="img" aria-label="Toy frog holding a heart"><span class="label">Cute<br>28</span></div>
        <div class="tile t-kids" role="img" aria-label="Two children on a blanket"><span class="label">Kids<br>92</span></div>
        <div class="tile t-ruins" role="img" aria-label="Stone building"></div>
        <div class="tile t-city" role="img" aria-label="Town under a blue sky"></div>
      </div>
    </div></div>
  </section>

  <section class="panel panel--editor">
    <div class="wave-band"></div>
    <svg class="feature-icon" viewBox="0 0 86 86" aria-hidden="true">
      <rect x="10" y="8" width="58" height="58" rx="5" fill="none" stroke="var(--icon)" stroke-width="5"/>
      <circle cx="28" cy="26" r="6" fill="none" stroke="var(--icon)" stroke-width="4"/>
      <path d="M50 78l4-14 22-22 10 10-22 22z" fill="none" stroke="var(--icon)" stroke-width="5" stroke-linejoin="round"/>
    </svg>
    <h2 class="title">Practical Editor</h2>
    <div class="device"><div class="screen">
      <div class="status-bar"><svg viewBox="0 0 6 6"><path d="M0 0h6L3 5z" fill="#fff"/></svg><svg viewBox="0 0 6 6"><path d="M6 0v6H0z" fill="#fff"/></svg><svg viewBox="0 0 6 6"><rect x="1.5" y="0" width="3" height="6" fill="#fff"/></svg><span>12:30</span></div>
      <div class="app-bar"><span class="name">Gallery</span><svg viewBox="0 0 8 8"><circle cx="3.2" cy="3.2" r="2.3" fill="none" stroke="#fff"/><line x1="5" y1="5" x2="7.5" y2="7.5" stroke="#fff"/></svg><svg viewBox="0 0 8 8"><circle cx="4" cy="1" r=".8" fill="#fff"/><circle cx="4" cy="4" r=".8" fill="#fff"/><circle cx="4" cy="7" r=".8" fill="#fff"/></svg></div>
      <div class="grid">
        <div class="tile t-scenery" role="img" aria-label="Sunset over a rocky coast"><span class="label">Scenery<br>276</span></div>
        <div class="tile t-garden" role="img" aria-label="Field of tulips"><span class="label">Garden<br>38</span></div>
        <div class="tile t-animal" role="img" aria-label="Puppy sitting on rocks"><span class="label">Animal<br>69</span></div>
        <div class="tile t-hiking" role="img" aria-label="Hiker in misty mountains"><span class="label">Hiking<br>154</span></div>
        <div class="tile t-cute" role="img" aria-label="Toy frog holding a heart"><span class="label">Cute<br>28</span></div>
        <div class="tile t-kids" role="img" aria-label="Two children on a blanket"><span class="label">Kids<br>92</span></div>
        <div class="tile t-ruins" role="img" aria-label="Stone building"></div>
        <div class="tile t-city" role="img" aria-label="Town under a blue sky"></div>
      </div>
    </div></div>
  </section>

  <section class="panel panel--custom">
    <div class="wave-band"></div>
    <svg class="feature-icon" viewBox="0 0 86 86" aria-hidden="true">
      <g stroke="var(--icon)" stroke-width="5" fill="none">
        <line x1="8" y1="16" x2="84" y2="16"/><circle cx="30" cy="16" r="7" fill="var(--orange)"/>
        <line x1="8" y1="43" x2="84" y2="43"/><circle cx="58" cy="43" r="7" fill="var(--orange)"/>
        <line x1="8" y1="70" x2="84" y2="70"/><circle cx="30" cy="70" r="7" fill="var(--orange)"/>
      </g>
    </svg>
    <h2 class="title">Customizable</h2>
    <div class="device"><div class="screen">
      <div class="status-bar"><svg viewBox="0 0 6 6"><path d="M0 0h6L3 5z" fill="#fff"/></svg><svg viewBox="0 0 6 6"><path d="M6 0v6H0z" fill="#fff"/></svg><svg viewBox="0 0 6 6"><rect x="1.5" y="0" width="3" height="6" fill="#fff"/></svg><span>12:30</span></div>
      <div class="app-bar"><span class="name">Gallery</span><svg viewBox="0 0 8 8"><circle cx="3.2" cy="3.2" r="2.3" fill="none" stroke="#fff"/><line x1="5" y1="5" x2="7.5" y2="7.5" stroke="#fff"/></svg><svg viewBox="0 0 8 8"><circle cx="4" cy="1" r=".8" fill="#fff"/><circle cx="4" cy="4" r=".8" fill="#fff"/><circle cx="4" cy="7" r=".8" fill="#fff"/></svg></div>
      <div class="grid">
        <div class="tile t-scenery" role="img" aria-label="Sunset over a rocky coast"><span class="label">Scenery<br>276</span></div>
        <div class="tile t-garden" role="img" aria-label="Field of tulips"><span class="label">Garden<br>38</span></div>
        <div class="tile t-animal" role="img" aria-label="Puppy sitting on rocks"><span class="label">Animal<br>69</span></div>
        <div class="tile t-hiking" role="img" aria-label="Hiker in misty mountains"><span class="label">Hiking<br>154</span></div>
        <div class="tile t-cute" role="img" aria-label="Toy frog holding a heart"><span class="label">Cute<br>28</span></div>
        <div class="tile t-kids" role="img" aria-label="Two children on a blanket"><span class="label">Kids<br>92</span></div>
        <div class="tile t-ruins" role="img" aria-label="Stone building"></div>
        <div class="tile t-city" role="img" aria-label="Town under a blue sky"></div>
      </div>
    </div></div>
  </section>

  <section class="panel panel--secure">
    <div class="wave-band"></div>
    <svg class="feature-icon" viewBox="0 0 86 86" aria-hidden="true">
      <path d="M43 6l32 12v22c0 20-14 34-32 42C25 74 11 60 11 40V18z" fill="none" stroke="var(--icon)" stroke-width="6" stroke-linejoin="round"/>
      <path d="M30 44l10 10 18-20" fill="none" stroke="var(--icon)" stroke-width="7" stroke-linecap="round" stroke-linejoin="round"/>
    </svg>
    <h2 class="title">Secure</h2>
    <div class="device"><div class="screen">
      <div class="status-bar"><svg viewBox="0 0 6 6"><path d="M0 0h6L3 5z" fill="#fff"/></svg><svg viewBox="0 0 6 6"><path d="M6 0v6H0z" fill="#fff"/></svg><svg viewBox="0 0 6 6"><rect x="1.5" y="0" width="3" height="6" fill="#fff"/></svg><span>12:30</span></div>
      <div class="app-bar"><span class="name">Gallery</span><svg viewBox="0 0 8 8"><circle cx="3.2" cy="3.2" r="2.3" fill="none" stroke="#fff"/><line x1="5" y1="5" x2="7.5" y2="7.5" stroke="#fff"/></svg><svg viewBox="0 0 8 8"><circle cx="4" cy="1" r=".8" fill="#fff"/><circle cx="4" cy="4" r=".8" fill="#fff"/><circle cx="4" cy="7" r=".8" fill="#fff"/></svg></div>
      <div class="grid">
        <div class="tile t-scenery" role="img" aria-label="Sunset over a rocky coast"><span class="label">Scenery<br>276</span></div>
        <div class="tile t-garden" role="img" aria-label="Field of tulips"><span class="label">Garden<br>38</span></div>
        <div class="tile t-animal" role="img" aria-label="Puppy sitting on rocks"><span class="label">Animal<br>69</span></div>
        <div class="tile t-hiking" role="img" aria-label="Hiker in misty mountains"><span class="label">Hiking<br>154</span></div>
        <div class="tile t-cute" role="img" aria-label="Toy frog holding a heart"><span class="label">Cute<br>28</span></div>
        <div class="tile t-kids" role="img" aria-label="Two children on a blanket"><span class="label">Kids<br>92</span></div>
        <div class="tile t-ruins" role="img" aria-label="Stone building"></div>
        <div class="tile t-city" role="img" aria-label="Town under a blue sky"></div>
      </div>
    </div></div>
  </section>

</main>
</body>
</html>
```